New design for Gift Ledger Website - landing page plus 3 carousel pages

We have a new website we want to launch for 501c3 organizations - Faith-based organizations, not for profit organizations, colleges and universities. Note - this is a design only project. We want to see designs for the landing page and the 3 other pages - Faith-based organizations, not for profit organizations, colleges and universities.
Format: We expect to create this website in Wix so requirement is to make the graphics Wix compatible
See Dossier attached for more details, 4 wireframes (1 landing page and 3 carousel pages), and brand guidelines
Please be creative and and make the visuals engaging. We do NOT want you to simply replicate what is in the wireframe. We are looking for a totally new, fresh and engaging design.
Look and feel
Each slider illustrates characteristics of the customer's brand and the style your logo design should communicate.

```html
<!DOCTYPE html>
<html lang="en">
<head>
<meta charset="utf-8">
<title>Gift Ledger – 501c3 Organizations</title>
<link href="https://fonts.googleapis.com/css2?family=League+Spartan:wght@500;600;700;800&family=Lato:wght@400;700&display=swap" rel="stylesheet">
<style>
:root{
  --navy:#0b1a3b;
  --navy-deep:#081530;
  --green:#14c68a;
  --green-dark:#0e8f66;
  --ink:#0b1a3b;
  --grey:#e7e8ea;
  --rule:#d3d6db;
  --white:#ffffff;
}
*{box-sizing:border-box;margin:0;padding:0}
html,body{width:1200px;height:4141px;overflow:hidden}
body{position:relative;background:var(--white);font-family:"Lato",sans-serif;color:var(--ink)}
.abs{position:absolute}
.center{left:0;right:0;text-align:center}
.head{font-family:"League Spartan",sans-serif;font-weight:700;letter-spacing:.5px}

/* header */
.site-header{position:absolute;top:0;left:0;width:1200px;height:105px;background:var(--white)}
.brand{position:absolute;display:flex;align-items:center;gap:12px;font-family:"League Spartan",sans-serif;font-weight:600;color:var(--navy)}
.brand .dot{width:44px;height:44px;border-radius:50%;background:var(--navy)}
.site-header .brand{left:84px;top:31px;font-size:30px}
.nav{position:absolute;top:44px;font-family:"League Spartan",sans-serif;font-weight:600;font-size:13px;color:var(--navy)}
.login{position:absolute;left:991px;top:29px;width:122px;height:50px;border:2px solid var(--navy);border-radius:25px;font-family:"League Spartan",sans-serif;font-weight:600;font-size:13px;display:flex;align-items:center;justify-content:center}

/* hero */
.hero{position:absolute;top:105px;left:0;width:1200px;height:590px;background:linear-gradient(180deg,var(--navy) 40%,#0c2a48 100%)}
.hero h1{top:90px;font-size:56px;color:var(--white);font-weight:800}
.hero .lead{top:166px;left:100px;right:100px;text-align:center;color:var(--white);font-size:14px;line-height:22px}
.hero-item{position:absolute;top:260px;width:260px;text-align:center}
.hero-item svg{display:block;margin:0 auto}
.hero-item p{margin-top:20px;color:var(--green);font-family:"League Spartan",sans-serif;font-weight:700;font-size:20px;line-height:27px}

/* diagram */
.diag-label{font-family:"League Spartan",sans-serif;font-weight:600;font-size:27px;line-height:38px;color:var(--navy)}

/* process */
.section-title{font-family:"League Spartan",sans-serif;font-weight:800;color:var(--navy);letter-spacing:.5px}
.step{position:absolute;top:1160px;width:250px;text-align:center}
.step svg{display:block;margin:0 auto}
.step h3{margin-top:18px;font-family:"League Spartan",sans-serif;font-weight:700;font-size:28px}
.step p{margin-top:12px;font-size:13px;line-height:21px;color:#2a3550;white-space:nowrap}
.btn{position:absolute;display:flex;align-items:center;justify-content:center;border-radius:30px;font-family:"League Spartan",sans-serif;font-weight:600;font-size:15px}
.btn-green{background:var(--green);color:var(--white)}

/* donation */
.donate{position:absolute;top:1609px;left:0;width:1200px;height:707px;background:linear-gradient(180deg,var(--navy) 55%,#0d2c4a 100%)}
.donate .title{top:92px;font-size:46px;color:var(--white)}
.donate .sub{top:150px;color:var(--white);font-size:16px}
.give{position:absolute;left:85px;top:250px;color:var(--white);font-family:"League Spartan",sans-serif;font-weight:700;font-size:27px}
.amount{position:absolute;height:44px;border:2px solid var(--green);border-radius:22px;color:var(--green);font-family:"League Spartan",sans-serif;font-weight:600;font-size:22px;display:flex;align-items:center;justify-content:center}
.cards{position:absolute;left:85px;top:452px;display:flex;gap:14px}
.card-chip{width:62px;height:32px;background:var(--white);border-radius:4px;display:flex;align-items:center;justify-content:center;font-size:11px;font-weight:700;color:var(--navy)}
.option{position:absolute;top:220px;width:277px;height:384px;background:var(--white);border-radius:14px;text-align:center}
.option svg{display:block;margin:38px auto 0}
.option h3{margin-top:22px;font-family:"League Spartan",sans-serif;font-weight:600;font-size:23px;line-height:30px;color:var(--navy)}
.option .brand{position:absolute;left:0;right:0;top:232px;justify-content:center;font-size:17px;gap:8px}
.option .brand .dot{width:28px;height:28px}
.btn-outline{border:2px solid var(--green);color:var(--green);font-size:13px}

/* why enroll */
.why-col{position:absolute;top:2536px;width:300px;text-align:center}
.why-col h3{margin-top:16px;font-family:"League Spartan",sans-serif;font-weight:700;font-size:29px}
.why-col p{margin-top:10px;font-size:13px;line-height:21px;color:#2a3550}
.vrule{position:absolute;top:2538px;height:170px;border-left:2px dashed var(--rule)}

/* newsletter */
.email{position:absolute;left:261px;top:3024px;width:677px;height:60px;background:var(--grey);border-radius:30px}
.email span{position:absolute;left:34px;top:21px;font-size:14px;color:#a3a7ae}
.send{position:absolute;left:795px;top:3024px;width:143px;height:60px;border-radius:30px;background:var(--navy);color:var(--white);font-family:"League Spartan",sans-serif;font-weight:600;font-size:15px;display:flex;align-items:center;justify-content:center}
.consent{position:absolute;left:302px;top:3098px;display:flex;align-items:center;gap:12px;font-size:15px;color:var(--navy)}
.box{width:20px;height:20px;border:2px solid var(--navy);border-radius:3px}
.fine{top:3135px;text-align:center;font-size:12.5px;line-height:17px;color:#2a3550;white-space:nowrap}

/* video */
.video{position:absolute;top:3290px;left:0;width:1200px;height:519px;background:radial-gradient(ellipse at 50% 60%,#3d6a4c 0%,#27384c 40%,#1b2636 100%)}

/* footer */
.footer-rule{position:absolute;left:84px;width:1029px;border-top:1px solid var(--rule)}
.footer-nav{position:absolute;top:4030px;left:0;right:0;display:flex;justify-content:center;gap:32px;font-family:"League Spartan",sans-serif;font-weight:600;font-size:13px;color:var(--navy)}
.copyright{top:4088px;font-size:13px;color:var(--navy);font-weight:700}
</style>
</head>
<body>

<header class="site-header">
  <div class="brand"><span class="dot"></span>Gift Ledger</div>
  <span class="nav" style="left:439px">ABOUT US&nbsp;⌄</span>
  <span class="nav" style="left:541px">NEWSROOM</span>
  <span class="nav" style="left:653px">PATENTS</span>
  <span class="nav" style="left:748px">CLIENTS</span>
  <span class="nav" style="left:833px">FAQ</span>
  <span class="nav" style="left:894px">CONTACT</span>
  <span class="login">LOG IN</span>
</header>

<section class="hero">
  <h1 class="abs center head">501c3 ORGANIZATIONS</h1>
  <p class="abs lead">Lorem ipsum dolor sit amet, consectetur adipiscing elit. Maecenas quam risus, semper non nunc nec, egestas tincidunt<br>quam. Duis eu nibh sit amet nisl imperdiet ornare at a neque.</p>

  <div class="hero-item" style="left:237px">
    <svg width="146" height="160" viewBox="0 0 146 160"><polygon points="73,8 138,44 138,116 73,152 8,116 8,44" fill="#fff" stroke="#0e8f66" stroke-width="6"/><g fill="#fff" stroke="#0e8f66" stroke-width="3"><circle cx="73" cy="8" r="6"/><circle cx="138" cy="44" r="6"/><circle cx="138" cy="116" r="6"/><circle cx="73" cy="152" r="6"/><circle cx="8" cy="116" r="6"/><circle cx="8" cy="44" r="6"/></g><circle cx="73" cy="80" r="32" fill="#14c68a" role="img" aria-label="Non profit community icon"/></svg>
    <p>NON PROFIT<br>ORGANISATION</p>
  </div>
  <div class="hero-item" style="left:468px">
    <svg width="146" height="160" viewBox="0 0 146 160"><polygon points="73,8 138,44 138,116 73,152 8,116 8,44" fill="#fff" stroke="#0e8f66" stroke-width="6"/><g fill="#fff" stroke="#0e8f66" stroke-width="3"><circle cx="73" cy="8" r="6"/><circle cx="138" cy="44" r="6"/><circle cx="138" cy="116" r="6"/><circle cx="73" cy="152" r="6"/><circle cx="8" cy="116" r="6"/><circle cx="8" cy="44" r="6"/></g><circle cx="73" cy="80" r="36" fill="#0b1a3b" role="img" aria-label="Faith symbols ring icon"/><circle cx="73" cy="80" r="14" fill="#fff"/></svg>
    <p>FAITH-BASED<br>ORGANIZATIONS</p>
  </div>
  <div class="hero-item" style="left:702px">
    <svg width="146" height="160" viewBox="0 0 146 160"><polygon points="73,8 138,44 138,116 73,152 8,116 8,44" fill="#fff" stroke="#0e8f66" stroke-width="6"/><g fill="#fff" stroke="#0e8f66" stroke-width="3"><circle cx="73" cy="8" r="6"/><circle cx="138" cy="44" r="6"/><circle cx="138" cy="116" r="6"/><circle cx="73" cy="152" r="6"/><circle cx="8" cy="116" r="6"/><circle cx="8" cy="44" r="6"/></g><rect x="45" y="52" width="56" height="56" rx="6" fill="#14c68a" role="img" aria-label="Graduate icon"/></svg>
    <p>COLLEGES<br>AND UNIVERSITIES</p>
  </div>
</section>

<div class="abs diag-label" style="left:135px;top:873px">501c3<br>ORGANIZATIONS</div>
<svg class="abs" style="left:370px;top:820px" width="470" height="190" viewBox="0 0 470 190">
  <g stroke="#9aa1ad" stroke-width="2" stroke-dasharray="10 6" fill="none">
    <line x1="0" y1="92" x2="351" y2="92"/>
    <line x1="351" y1="7" x2="351" y2="179"/>
    <line x1="351" y1="7" x2="454" y2="7"/>
    <line x1="351" y1="179" x2="454" y2="179"/>
  </g>
</svg>
<div class="abs diag-label" style="left:836px;top:788px">DATA OBJECT<br>"DONOR"</div>
<div class="abs diag-label" style="left:836px;top:960px">DATA EXCHANGE<br>"BUYER"</div>

<h2 class="abs center section-title" style="top:1082px;font-size:43px">PROCESS</h2>
<svg class="abs" style="left:250px;top:1210px" width="700" height="16" viewBox="0 0 700 16">
  <g stroke="#9aa1ad" stroke-width="2" fill="none">
    <line x1="4" y1="8" x2="168" y2="8" stroke-dasharray="8 6"/><polyline points="80,2 87,8 80,14"/>
    <line x1="266" y1="8" x2="430" y2="8" stroke-dasharray="8 6"/><polyline points="344,2 351,8 344,14"/>
    <line x1="530" y1="8" x2="694" y2="8" stroke-dasharray="8 6"/><polyline points="608,2 615,8 608,14"/>
  </g>
</svg>
<div class="step" style="left:79px"><svg width="96" height="110" viewBox="0 0 96 110"><polygon points="48,4 92,29 92,81 48,106 4,81 4,29" fill="#0b1a3b" stroke="#14c68a" stroke-width="5"/><text x="48" y="66" text-anchor="middle" font-family="League Spartan" font-weight="700" font-size="32" fill="#14c68a">01</text></svg><h3>Step 1</h3><p>Lorem ipsum dolor sit amet,<br>consectetur adipiscing elit. Maecenas<br>quam risus, semper</p></div>
<div class="step" style="left:341px"><svg width="96" height="110" viewBox="0 0 96 110"><polygon points="48,4 92,29 92,81 48,106 4,81 4,29" fill="#0b1a3b" stroke="#14c68a" stroke-width="5"/><text x="48" y="66" text-anchor="middle" font-family="League Spartan" font-weight="700" font-size="32" fill="#14c68a">02</text></svg><h3>Step 2</h3><p>Lorem ipsum dolor sit amet,<br>consectetur adipiscing elit. Maecenas<br>quam risus, semper</p></div>
<div class="step" style="left:605px"><svg width="96" height="110" viewBox="0 0 96 110"><polygon points="48,4 92,29 92,81 48,106 4,81 4,29" fill="#0b1a3b" stroke="#14c68a" stroke-width="5"/><text x="48" y="66" text-anchor="middle" font-family="League Spartan" font-weight="700" font-size="32" fill="#14c68a">03</text></svg><h3>Step 3</h3><p>Lorem ipsum dolor sit amet,<br>consectetur adipiscing elit. Maecenas<br>quam risus, semper</p></div>
<div class="step" style="left:869px"><svg width="96" height="110" viewBox="0 0 96 110"><polygon points="48,4 92,29 92,81 48,106 4,81 4,29" fill="#0b1a3b" stroke="#14c68a" stroke-width="5"/><text x="48" y="66" text-anchor="middle" font-family="League Spartan" font-weight="700" font-size="32" fill="#14c68a">04</text></svg><h3>Step 4</h3><p>Lorem ipsum dolor sit amet,<br>consectetur adipiscing elit. Maecenas<br>quam risus, semper</p></div>
<span class="btn btn-green" style="left:500px;top:1448px;width:194px;height:57px">DONATE DATA</span>

<section class="donate">
  <h2 class="abs center section-title title">MY DONATION</h2>
  <p class="abs center sub">All donations are tax deductible</p>
  <div class="give">I want to give</div>
  <span class="amount" style="left:85px;top:302px;width:111px">$25</span>
  <span class="amount" style="left:209px;top:302px;width:111px">$50</span>
  <span class="amount" style="left:336px;top:302px;width:111px">$100</span>
  <span class="amount" style="left:85px;top:368px;width:111px">$125</span>
  <span class="amount" style="left:209px;top:368px;width:111px">$150</span>
  <span class="amount" style="left:336px;top:368px;width:151px;font-size:15px">Other Amount</span>
  <div class="cards">
    <span class="card-chip">Orbit</span><span class="card-chip">Kestrel</span><span class="card-chip">Lumen</span><span class="card-chip">Meridian</span><span class="card-chip">Ferrypay</span>
  </div>
  <span class="btn btn-green" style="left:85px;top:518px;width:264px;height:56px;font-size:14px">DONATE WITH CREDIT CARD</span>

  <div class="option" style="left:532px">
    <svg width="96" height="110" viewBox="0 0 96 110"><polygon points="48,4 92,29 92,81 48,106 4,81 4,29" fill="#14c68a"/><circle cx="48" cy="55" r="18" fill="none" stroke="#fff" stroke-width="3"/><circle cx="48" cy="55" r="6" fill="#fff"/></svg>
    <h3>Donate with Crypto<br>Powered by GLT</h3>
    <div class="brand"><span class="dot"></span>Gift Ledger</div>
    <span class="btn btn-outline" style="left:78px;top:294px;width:122px;height:50px">DONATE</span>
  </div>
  <div class="option" style="left:836px">
    <svg width="96" height="110" viewBox="0 0 96 110"><polygon points="48,4 92,29 92,81 48,106 4,81 4,29" fill="#14c68a"/><g fill="none" stroke="#fff" stroke-width="3"><rect x="30" y="50" width="36" height="9" rx="3"/><rect x="30" y="62" width="36" height="9" rx="3"/><rect x="30" y="74" width="36" height="9" rx="3"/><path d="M34 46a14 12 0 0 1 28 0"/></g></svg>
    <h3>Donate with Data</h3>
    <div class="brand"><span class="dot"></span>Gift Ledger</div>
    <span class="btn btn-outline" style="left:78px;top:294px;width:122px;height:50px">DONATE</span>
  </div>
</section>

<h2 class="abs center section-title" style="top:2410px;font-size:45px">WHY ENROLL!</h2>
<p class="abs center" style="top:2470px;font-size:15px">To get full access to all the features, start by creating an account</p>
<div class="why-col" style="left:98px">
  <svg width="70" height="70" viewBox="0 0 70 70" fill="none" stroke="#0b1a3b" stroke-width="4"><rect x="5" y="10" width="60" height="55" rx="5"/><line x1="5" y1="22" x2="65" y2="22" stroke="#14c68a" stroke-width="6"/><line x1="18" y1="3" x2="18" y2="14"/><line x1="52" y1="3" x2="52" y2="14"/><g stroke-width="5" stroke-dasharray="4 6"><line x1="14" y1="34" x2="58" y2="34"/><line x1="14" y1="44" x2="58" y2="44"/><line x1="14" y1="54" x2="58" y2="54"/></g></svg>
  <h3>Drops</h3><p>Purchase NFTs that are directly sold<br>by top Creators</p>
</div>
<div class="vrule" style="left:424px"></div>
<div class="why-col" style="left:450px">
  <svg width="70" height="70" viewBox="0 0 70 70" fill="none" stroke="#0b1a3b" stroke-width="4"><rect x="5" y="5" width="60" height="14" rx="3" stroke="#14c68a"/><path d="M5 19v6a7 7 0 0 0 15 0a7 7 0 0 0 15 0a7 7 0 0 0 15 0a7 7 0 0 0 15 0v-6"/><path d="M10 34v31h50V34"/><rect x="26" y="44" width="18" height="21"/></svg>
  <h3>Marketplace</h3><p>Bid on and auction off rare digital<br>collectibles</p>
</div>
<div class="vrule" style="left:776px"></div>
<div class="why-col" style="left:801px">
  <svg width="70" height="70" viewBox="0 0 70 70"><polygon points="35,3 64,19 64,51 35,67 6,51 6,19" fill="none" stroke="#0b1a3b" stroke-width="4"/><text x="35" y="42" text-anchor="middle" font-family="League Spartan" font-weight="700" font-size="19" fill="#14c68a">NFT</text></svg>
  <h3>My NFTs</h3><p>A digital gallery to showcase your<br>collection</p>
</div>
<div class="abs" style="left:0;top:2812px;width:1200px;border-top:2px solid var(--grey)"></div>

<h2 class="abs center section-title" style="top:2905px;font-size:48px">NEVER MISS A DROP</h2>
<p class="abs center" style="top:2966px;font-size:16px">Subscribe for the latest news, drops &amp; collectibles</p>
<div class="email"><span>Email</span></div>
<span class="send">SEND</span>
<div class="consent"><span class="box"></span>By entering my email and subscribing I confirm and agree to the above.</div>
<p class="abs center fine">After rending the Privacy Notice, you may subscribe for our newsletter to get special offers and<br>occasional surveys delivered to your inbox. Unsubscribe at any time by clicking<br>on the link in the email.</p>

<section class="video" role="img" aria-label="Video still: finger pressing a green Donate key on a keyboard">
  <svg class="abs" style="left:530px;top:189px" width="140" height="140" viewBox="0 0 140 140"><circle cx="70" cy="70" r="66" fill="#fff" stroke="#dfe3e6" stroke-width="6"/><polygon points="56,46 98,70 56,94" fill="#14c68a"/></svg>
</section>

<footer>
  <div class="brand" style="left:470px;top:3922px;font-size:30px"><span class="dot"></span>Gift Ledger</div>
  <div class="footer-rule" style="top:4013px"></div>
  <nav class="footer-nav"><span>ABOUT US</span><span>NEWSROOM</span><span>PATENTS</span><span>CLIENTS</span><span>FAQ</span><span>CONTACT</span></nav>
  <div class="footer-rule" style="top:4065px"></div>
  <p class="abs center copyright">Copyright 2022.Alll right reserved</p>
</footer>

</body>
</html>
```